Wine Label for a Prosecco Wine Called Vuro

Prosecco is a white sparkling wine from Italy. We are looking for an eye catching, elegant label for this prosecco that is called "Vuro" because it is a young, fresh, lively white sparkling wine. (We do not want to see children or babies featured on the label-- just the name VURO please.) Attached is the old label for your reference, and the bottle type that will be used , which is a dark green Burgundy style bottle (pls ignore the label on the bottle). Please no grapes or wine glasses on the label. We are looking for something: eye catching / fun / ELEGANT (not cheap). We would be happy with a fun color too. Remember-- elegant, eye catching! Thanks!
Updates

Hi All, I think I made a mistake in my brief and have updated it. I also uploaded a competitor's label that we like very much to give better direction to what we are looking for. Also, the word Vuro cannot be vertical, nor can it be broken. It needs to read: VURO or Vuro. Thanks

Target Market(s)

American adults male and female.

Colors
abd036
33a6d7
33b8a4
ffcf3e

Requirements
Must have
• The mandatory information as shown on old labels. The word VURO should be very prominent.
Nice to have
• The uploaded photo of a competitor's prosecco shows a label we really like... if you could play around with this shape and style we'd be very happy.
Should not have
• No grape images, no wine glass images, no images of babies or children.

```html
<!DOCTYPE html>
<html lang="it">
<head>
<meta charset="utf-8">
<title>Vuro Prosecco – Wine Label</title>
<link rel="stylesheet" href="https://fonts.googleapis.com/css2?family=Audiowide&family=Yellowtail&family=Roboto:wght@300;400&display=swap">
<style>
  :root {
    --page-bg: #1c1c1c;
    --label-black: #0b0b0b;
    --stone-dark: #1a1a1a;
    --stone-mid: #2b2b2b;
    --lava-red: #c8250e;
    --lava-orange: #ff7a3c;
    --gold-line: #f0a21c;
    --script-gold: #f7b21e;
    --text-light: #f2f2f2;
    --edge-grey: #5a5a5a;
  }
  * { margin: 0; padding: 0; box-sizing: border-box; }
  html, body {
    width: 1200px;
    height: 800px;
    overflow: hidden;
    background: var(--page-bg);
  }
  .canvas {
    width: 1200px;
    height: 800px;
    display: flex;
    align-items: center;
    justify-content: center;
  }
  .label {
    position: relative;
    width: 556px;
    height: 700px;
    background: var(--label-black);
    border: 3px solid var(--edge-grey);
    box-shadow: 0 0 0 1px #000, 0 10px 30px rgba(0,0,0,0.6);
    overflow: hidden;
  }
  .label__texture {
    position: absolute;
    left: 0; top: 0;
    width: 100%;
    height: 400px;
    background:
      radial-gradient(ellipse at 30% 25%, rgba(200,37,14,0.35), transparent 55%),
      radial-gradient(ellipse at 75% 80%, rgba(200,37,14,0.3), transparent 50%),
      linear-gradient(160deg, var(--stone-mid), var(--stone-dark));
  }
  .label__name {
    position: absolute;
    left: 0; right: 0;
    top: 138px;
    text-align: center;
    font-family: "Audiowide", sans-serif;
    font-size: 128px;
    line-height: 1;
    letter-spacing: 4px;
    color: var(--lava-orange);
  }
  .label__rule {
    position: absolute;
    left: 0; right: 0;
    height: 4px;
    background: var(--gold-line);
  }
  .label__rule--upper { top: 406px; }
  .label__rule--lower { top: 543px; }
  .label__band {
    position: absolute;
    left: 0; right: 0;
    top: 410px;
    height: 133px;
    background: var(--label-black);
    display: flex;
    align-items: center;
    justify-content: center;
  }
  .label__wine-type {
    font-family: "Yellowtail", cursive;
    font-size: 78px;
    color: var(--script-gold);
    letter-spacing: 3px;
  }
  .label__footer {
    position: absolute;
    left: 0; right: 0;
    top: 547px;
    bottom: 0;
    background: linear-gradient(180deg, #1e1e1e, #111);
  }
  .label__details {
    position: absolute;
    left: 0; right: 0;
    top: 565px;
    text-align: center;
    color: var(--text-light);
    font-family: "Roboto", sans-serif;
    font-weight: 300;
  }
  .label__region { font-size: 30px; line-height: 1.2; }
  .label__classification { font-size: 21px; margin-top: 6px; }
  .label__style { font-size: 21px; margin-top: 8px; letter-spacing: 1px; }
</style>
</head>
<body>
  <main class="canvas">
    <article class="label">
      <div class="label__texture" role="img" aria-label="Dark cracked volcanic stone texture with glowing red and orange lava veins"></div>
      <h1 class="label__name">VURO</h1>
      <div class="label__rule label__rule--upper"></div>
      <div class="label__band">
        <p class="label__wine-type">PROSECCO</p>
      </div>
      <div class="label__rule label__rule--lower"></div>
      <div class="label__footer" role="img" aria-label="Dark hexagonal mesh pattern"></div>
      <div class="label__details">
        <p class="label__region">Veneto</p>
        <p class="label__classification">Indicazione Geografica Tipica</p>
        <p class="label__style">FRIZZANTE</p>
      </div>
    </article>
  </main>
</body>
</html>
```